Skincare Product Packaging Box Design

tall meadow skincare is launching an acne kit to help clear people's skin. The shipping box needs to communicate our brand values and look amazing. We intend on using this acne kit as a subscription service for acne treatment. The shipping box size is 10 x 6 x 3. We have a dieline template for the box, but first we'd like to see your design idea overlaid on the 3 dimensional box, then if we choose your design that would need to be put on the dieline template.

As far as the colors we'd like to use - we should have some elements of the colors of our brand, but feel free to try other colors as well.

Target Market(s)

All ages, ethnicities and genders. Basically anyone with acne.

Industry/Entity Type

Skin Care Product

Font styles to use
Sans Serif

Requirements
Must have
• 1. Design must be gender neutral.
2. We want irregular shapes of color on the box.
3. We need "acne kit" written to describe the box.
4. Must have the tall meadow logo (please take the logo off of file #10).
5. Use the colors for the box design from the first file titled "use these colors".
6. Use the 3 dimensional box image to represent your idea
Nice to have
• vibrant, no pics of acne, try to focus on appealing to all races and genders. Focus on images of the products with vibrant colors in the background. We are not sure if we want images of our products to be included on the box or not. I have attached images of our products so that you have an idea of our branding. But the attached products are not the actual ones that will be going into the kit.
Should not have
• No lotus flowers. No stock images of super attractive women with cream on their face and cucumbers. No cheesy stock images of an outline of a face.

```html
<!DOCTYPE html>
<html lang="en">
<head>
<meta charset="utf-8">
<title>tall meadow skincare – Acne Kit box lid</title>
<link rel="stylesheet" href="https://fonts.googleapis.com/css2?family=Oswald:wght@600&family=Michroma&display=swap">
<style>
  :root {
    --teal: #06a9a7;
    --teal-deep: #05908e;
    --orange: #e6891d;
    --grey: #67676a;
    --white: #f4f4f4;
    --line: #ffffff;
  }
  html, body {
    margin: 0;
    padding: 0;
    width: 1200px;
    height: 778px;
    overflow: hidden;
    background: var(--teal);
  }
  .box-lid {
    position: relative;
    width: 1200px;
    height: 778px;
    overflow: hidden;
    background: var(--teal);
  }
  .box-lid__shapes {
    position: absolute;
    inset: 0;
    width: 1200px;
    height: 778px;
  }
  .brand-name {
    position: absolute;
    left: 0;
    right: 0;
    top: 205px;
    margin: 0;
    text-align: center;
    font-family: "Oswald", "Arial Narrow", sans-serif;
    font-weight: 600;
    color: var(--grey);
    font-size: 92px;
    line-height: 0.95;
    letter-spacing: 1px;
    text-transform: uppercase;
  }
  .product-label {
    position: absolute;
    left: 315px;
    top: 455px;
    width: 570px;
    height: 72px;
    background: var(--white);
    display: flex;
    align-items: center;
    justify-content: center;
  }
  .product-label__text {
    margin: 0;
    font-family: "Michroma", "Arial", sans-serif;
    font-size: 36px;
    letter-spacing: 6px;
    color: var(--grey);
    text-transform: uppercase;
  }
</style>
</head>
<body>
<main class="box-lid">
  <svg class="box-lid__shapes" viewBox="0 0 1200 778" aria-hidden="false">
    <!-- orange corner blob -->
    <path class="shape-orange" fill="var(--orange)"
      d="M660 0 C700 60 760 90 840 100 C930 112 1010 130 1080 200 C1130 250 1160 300 1200 330 L1200 0 Z"/>
    <path class="curve-orange" fill="none" stroke="var(--line)" stroke-width="2.5"
      d="M640 0 C690 80 770 112 860 126 C960 142 1040 170 1110 250 C1150 296 1175 320 1200 338"/>
    <!-- grey corner blob -->
    <path class="shape-grey" fill="var(--grey)"
      d="M0 470 C60 430 160 420 230 470 C300 520 300 590 360 640 C410 682 470 720 520 778 L0 778 Z"/>
    <path class="curve-grey" fill="none" stroke="var(--line)" stroke-width="2.5"
      d="M60 560 C110 640 200 640 280 660 C360 680 410 720 450 778"/>
    <!-- decorative dash and dot clusters -->
    <rect class="pattern-area" role="img" aria-label="Cluster of teal brush-dash marks on the orange shape"
      x="920" y="20" width="140" height="90" rx="45" fill="var(--teal-deep)" opacity="0.55"/>
    <rect class="pattern-area" role="img" aria-label="Cluster of grey brush-dash marks in the upper left corner"
      x="20" y="20" width="110" height="150" rx="50" fill="var(--grey)" opacity="0.55"/>
    <rect class="pattern-area" role="img" aria-label="Cluster of orange pebble dots on the right edge"
      x="1080" y="420" width="110" height="170" rx="50" fill="var(--orange)" opacity="0.8"/>
  </svg>

  <h1 class="brand-name">Tall Meadow<br>Skincare</h1>

  <div class="product-label">
    <p class="product-label__text">Acne Kit</p>
  </div>
</main>
</body>
</html>
```